Homes, Invest in Non-performing loans

We need only 3 web pages, one for the home, one for the content, one for the properties.
The main focus of our business is to offer non performing loans (before foreclosures) to the general public. All the non-performing mortgages will end in a house, an apartment, a store, etc.
Our customers are able to invest from 10,000usd to 1,000,000usd (average 50,000usd).
Our customers' usual focus groups are employees who want second earnings, perceiving the business feeling without outlay time. They look for a solid finance sense corporation that confers them certainty.
Nearly all our clients desire the house, apartment, store, etc. more than the actual earnings.
The name of our company is BRAMLEY
Reason: We value the time and effort you already invest in our project. We realize that we did't come back on some of the doubts requested by the designers. It will be inequitable to the designers who prerequisite our feedback. We also appreciate the comprehension of the community in this postponement.
Reason: Designers,
We really apreciate all the time and effort you put on our project. From the begining we ask for 3 pages, so now we will leave the 10 finalist and provide some extra time to submit the other 2 pages.
We will race the price in 10%
Target Market(s)
Our customers average investors works as employees and want to have a second income or business without spending time. (People from 35 to 50)
Industry/Entity Type
Finance
Requirements
Should not have
- FLASH

```html
<!DOCTYPE html>
<html lang="en">
<head>
<meta charset="utf-8">
<title>Bramley — Remates Hipotecarios</title>
<link href="https://fonts.googleapis.com/css2?family=Ubuntu:wght@400;500&family=Lustria&display=swap" rel="stylesheet">
<style>
:root{
  --page-bg:#e4e0d8;
  --column-bg:#d8d4cb;
  --white:#ffffff;
  --olive:#807d16;
  --olive-light:#8e8b22;
  --charcoal:#4b4a4a;
  --tile:#585757;
  --tile-rim:#7a7979;
  --text:#595959;
  --text-dark:#3a3a3a;
  --band:#f2eee8;
  --field:#efe8e1;
  --news-bg:#f1f1f0;
}
*{box-sizing:border-box;margin:0;padding:0}
html,body{width:1200px;height:938px;overflow:hidden}
body{background:var(--page-bg);font-family:"Ubuntu",sans-serif;color:var(--text);position:relative}
.column{position:absolute;left:204px;top:0;width:792px;height:938px;background:var(--column-bg)}
.sheet{position:absolute;left:220px;top:0;width:760px;height:878px;background:var(--white)}
.abs{position:absolute}

/* header */
.brand{left:246px;top:22px;width:90px}
.brand-name{font-size:22px;font-weight:500;color:var(--charcoal);letter-spacing:1px;display:flex;align-items:center;gap:6px}
.brand-name i{display:block;width:14px;height:14px;background:var(--olive)}
.brand-tag{font-size:6px;letter-spacing:1px;color:var(--charcoal);margin-top:22px}
.call{left:604px;top:21px;font-size:14px;color:var(--olive)}
.call b{font-weight:400;color:var(--text-dark)}
.search{left:790px;top:19px;width:152px;height:18px;border:1px solid #cfcfcf;border-radius:3px;font-size:9px;color:#999;padding:3px 8px}
.go{left:946px;top:19px;width:26px;height:18px;background:var(--charcoal);color:#fff;font-size:9px;text-align:center;line-height:18px;border-radius:3px}
.nav{top:65px;height:21px;background:var(--charcoal);color:#fff;font-size:12.5px;text-align:center;line-height:22px}
.nav::before{content:"";position:absolute;left:50%;top:-5px;margin-left:-5px;border:5px solid transparent;border-top:0;border-bottom-color:var(--charcoal)}
.nav.active{background:var(--olive)}
.nav.active::before{border-bottom-color:var(--olive)}

/* hero */
.hero{left:227px;top:96px;width:746px;height:228px;background:linear-gradient(90deg,#9fb4c9 0%,#4a4d55 25%,#6f6f72 48%,#b9b8b6 62%,#e7e6e4 72%,#ececea 100%)}
.hero-arrow{top:190px;width:20px;height:38px;background:#5b5b5b}
.hero-arrow.left{left:210px;border-radius:19px 0 0 19px}
.hero-arrow.right{left:973px;border-radius:0 19px 19px 0}
.hero-title{left:712px;top:131px;width:261px;height:48px;background:rgba(120,120,120,.78);color:#fff;font-family:"Lustria",serif;font-size:19px;line-height:48px;padding-left:26px;text-shadow:1px 1px 2px #333}
.hero-copy{left:710px;top:196px;width:256px;font-family:"Lustria",serif;font-size:14.5px;line-height:24px;color:var(--text-dark);text-align:justify}

/* welcome */
.welcome{left:232px;top:332px;font-size:16px;color:var(--text-dark)}
.welcome span{color:var(--olive)}
.welcome small{font-size:9px;margin-right:6px}
.rule{left:229px;top:358px;width:483px;border-top:1px dashed #cfcfcf}
.intro{left:229px;top:366px;width:509px;font-size:10.3px;line-height:13.6px;text-align:justify}
.intro p{margin-bottom:13.6px}

/* services cluster */
.tile{width:100px;height:100px;background:var(--tile);border:6px solid var(--tile-rim);color:#fff;font-family:"Lustria",serif;font-size:12px;line-height:16px;text-align:center;padding-top:18px}
.tile.tl{left:754px;top:333px;border-radius:16px 16px 4px 16px}
.tile.tr{left:868px;top:333px;border-radius:16px 16px 16px 4px}
.tile.bl{left:754px;top:447px;border-radius:16px 4px 16px 16px;padding-top:36px}
.tile.br{left:868px;top:447px;border-radius:4px 16px 16px 16px;padding-top:38px}
.hub{left:811px;top:390px;width:100px;height:100px;border-radius:50%;background:var(--olive-light);border:5px solid #fff;color:#fff;font-family:"Lustria",serif;font-size:12px;line-height:16px;text-align:center;padding-top:20px}

/* feature band */
.band{left:226px;top:560px;width:748px;height:220px;background:var(--band)}
.card{top:570px;width:192px;height:198px;background:#fff;border:1px solid #e2ddd5;padding:7px}
.card .photo{width:176px;height:94px}
.card h3{font-weight:400;font-size:12px;color:var(--olive);margin:12px 0 4px}
.card p{font-size:9.6px;line-height:13.6px}
.card .more{margin-top:6px;width:78px;height:16px;background:var(--charcoal);color:#fff;font-size:9.5px;line-height:16px;padding-left:6px}
.contacts{left:836px;top:572px;width:128px;height:122px;background:#f5f1ec;padding:10px 8px;font-size:9.5px;color:var(--text-dark)}
.contacts .row{display:flex;align-items:center;gap:5px;margin-top:4px}
.contacts .row.msg{color:var(--olive)}
.contacts .label{margin-top:12px}
.contacts .label:first-child{margin-top:0}
.follow{left:837px;top:704px;font-size:12px;color:var(--text)}
.social{top:728px;width:22px;height:22px;background:var(--charcoal);border-radius:3px}

/* news & signup */
.news{left:228px;top:790px;width:558px;height:79px;background:var(--news-bg);border:1px solid #e0e0e0;border-radius:3px;padding:6px 10px}
.news h4{font-weight:400;font-size:12px;color:var(--olive)}
.news .date{font-size:10.5px;color:var(--olive);margin-top:5px}
.news p{font-size:9.8px;color:var(--text-dark);line-height:16px;margin-top:3px;padding-left:2px}
.start{left:794px;top:786px;font-size:12px;color:var(--olive)}
.field{left:798px;width:172px;height:18px;background:var(--field);border-radius:3px;font-size:10px;color:var(--text-dark);padding:2px 9px}
.submit{left:798px;top:850px;width:68px;height:17px;background:#6d6d6d;color:#fff;border-radius:3px;font-size:11px;line-height:17px;padding-left:14px}

/* footer */
.footer-nav{left:0;top:888px;width:1200px;text-align:center;font-size:10.5px;color:var(--text-dark);word-spacing:2px}
.footer-nav span{margin:0 11px}
.copyright{left:0;top:914px;width:1200px;text-align:center;font-size:10.5px;color:var(--text-dark)}
</style>
</head>
<body>
<div class="column"></div>
<div class="sheet"></div>

<header>
  <div class="abs brand">
    <div class="brand-name"><i></i>BRAMLEY</div>
    <div class="brand-tag">REMATES HIPOTECARIOS</div>
  </div>
  <div class="abs call">Call us today : <b>555·010·0420</b></div>
  <div class="abs search">Search :</div>
  <div class="abs go">GO</div>
  <nav>
    <div class="abs nav active" style="left:358px;width:70px">Home</div>
    <div class="abs nav" style="left:435px;width:66px">Loans</div>
    <div class="abs nav" style="left:510px;width:70px">About</div>
    <div class="abs nav" style="left:588px;width:102px">Our Services</div>
    <div class="abs nav" style="left:698px;width:71px">FAQs</div>
    <div class="abs nav" style="left:777px;width:93px">Resources</div>
    <div class="abs nav" style="left:878px;width:94px">Contact Us</div>
  </nav>
</header>

<section>
  <div class="abs hero" role="img" aria-label="Photo of a smiling team of business professionals in suits"></div>
  <svg class="abs hero-arrow left" viewBox="0 0 20 38"><path d="M14 13 L7 19 L14 25 Z" fill="#fff"/></svg>
  <svg class="abs hero-arrow right" viewBox="0 0 20 38"><path d="M6 13 L13 19 L6 25 Z" fill="#fff"/></svg>
  <div class="abs hero-title">Value to your business</div>
  <div class="abs hero-copy">The only independent Banking Group specializing in the value chain of the trade receivables, non–performing loans, and tax receivables »</div>
</section>

<section>
  <h1 class="abs welcome" style="font-weight:400"><small>»</small>Welcome to <span>Bramley</span></h1>
  <div class="abs rule"></div>
  <div class="abs intro">
    <p>Lorem Ipsum is simply dummy text of the printing and typesetting industry. Lorem Ipsum has been the industry's standard dummy text ever since the 1500s, when an unknown printer took a galley of type and scrambled it to make a type specimen book.</p>
    <p>&nbsp;It has survived not only five centuries, but also the leap into electronic typesetting, remaining essentially unchanged. It was popularised in the 1960s with the release of Lettrex sheets containing Lorem Ipsum passages, and more recently with desktop publishing software like Folio Layout including versions of Lorem Ipsum.and more recently with desktop publishing software like Folio Layout including versions of Lorem Ipsum.</p>
    <p>Lorem Ipsum is simply dummy text of the printing and typesetting industry. Lorem Ipsum has been the industry's standard dummy text ever since the 1500s, when an unknown printer took a galley of type and scrambled it to make a type specimen book.</p>
  </div>
  <div class="abs tile tl">Marketing<br>Information</div>
  <div class="abs tile tr">Risk<br>Information</div>
  <div class="abs tile bl">Payment<br>Services</div>
  <div class="abs tile br">Receivable<br>Managment</div>
  <div class="abs hub">Serving<br>clients<br>Securing cash</div>
</section>

<section>
  <div class="abs band"></div>
  <article class="abs card" style="left:234px">
    <div class="photo" role="img" aria-label="Photo of business people shaking hands" style="background:linear-gradient(135deg,#dfe4ea,#2f3a4f 55%,#cfd5dd)"></div>
    <h3>About Us</h3>
    <p>Lorem Ipsum is simply dummy text of the printing and typesetting industry. Lorem Ipsum has ce the 1500s.</p>
    <div class="more">» Read More</div>
  </article>
  <article class="abs card" style="left:435px">
    <div class="photo" role="img" aria-label="Photo of a woman working on a laptop" style="background:linear-gradient(135deg,#e8dcc0,#c9a86e 45%,#f3f1ec)"></div>
    <h3>Loan Application Form</h3>
    <p>Lorem Ipsum is simply dummy text of the printing and typesetting industry. Lorem Ipsum has ce the 1500s.</p>
    <div class="more">» Read More</div>
  </article>
  <article class="abs card" style="left:636px">
    <div class="photo" role="img" aria-label="Photo of a large group of smiling clients" style="background:linear-gradient(180deg,#e9e9e9,#8a6f66 45%,#5d6f8a)"></div>
    <h3>Testimonials</h3>
    <p>Lorem Ipsum is simply dummy text of the printing and typesetting industry. Lorem Ipsum has ce the 1500s.</p>
    <div class="more">» Read More</div>
  </article>
  <aside class="abs contacts">
    <div class="label">Debtors</div>
    <div class="row"><svg width="11" height="11" viewBox="0 0 11 11"><rect width="11" height="11" fill="#9a9a9a"/><path d="M3 2h2v2l-1 1c.5 1 1 1.5 2 2l1-1h2v2c-4 0-6-2-6-6z" fill="#fff"/></svg>+49 30&nbsp; 55-0101</div>
    <div class="row msg"><svg width="11" height="11" viewBox="0 0 11 11"><rect width="11" height="11" fill="#9a9a9a"/><path d="M2 3h7v5H2z M2 3l3.5 3L9 3" fill="none" stroke="#fff"/></svg>Send message</div>
    <div class="label">Customers</div>
    <div class="row"><svg width="11" height="11" viewBox="0 0 11 11"><rect width="11" height="11" fill="#9a9a9a"/><path d="M3 2h2v2l-1 1c.5 1 1 1.5 2 2l1-1h2v2c-4 0-6-2-6-6z" fill="#fff"/></svg>+49 555-0102</div>
    <div class="row msg"><svg width="11" height="11" viewBox="0 0 11 11"><rect width="11" height="11" fill="#9a9a9a"/><path d="M2 3h7v5H2z M2 3l3.5 3L9 3" fill="none" stroke="#fff"/></svg>Send message</div>
  </aside>
  <div class="abs follow">» Follow Us</div>
  <div class="abs social" style="left:839px" aria-label="Social network"></div>
  <div class="abs social" style="left:868px" aria-label="Social network"></div>
  <div class="abs social" style="left:898px" aria-label="Social network"></div>
  <div class="abs social" style="left:926px" aria-label="News feed"></div>
</section>

<section>
  <div class="abs news">
    <h4>» Latest News</h4>
    <div class="date">13.09.2012 Norvale remains on a growth course</div>
    <p>In issue 4/2012 you can find out more about: A new magazine for corporate financing Service for online traders<br>Debt collection services in Eastern Europe ...</p>
  </div>
  <div class="abs start">» Let's Get Started</div>
  <div class="abs field" style="top:806px">Name :</div>
  <div class="abs field" style="top:828px">Email :</div>
  <div class="abs submit">Submit</div>
</section>

<footer>
  <div class="abs footer-nav">Home<span>|</span>Loans<span>|</span>About<span>|</span>Our Services<span>|</span>FAQs<span>|</span>Resources<span>|</span>Contact<span>|</span>Blog</div>
  <div class="abs copyright">Copyright© 2012 by Bramley</div>
</footer>
</body>
</html>
```